Launch of a new Investment fund

Im looking for someone design a logo and website for my Investment fund located in Singapore.

Attached to this project you will find a project scope document that details exactly what i am looking for and also includes a website copy that i have written up. I am happy for you to take your own inspiration as well to design the website. At this stage the website wont be very detailed as there isn't much information to showcase. I will require the website to be easily editable in the future so i can update it with progress the fund makes.

If you require any further details on the project please reach out to me

Coding

Coded - Design and coding required

Number of Pages Required

4 page

```html
<!DOCTYPE html>
<html lang="en">
<head>
<meta charset="utf-8">
<title>Northvale Capital Management</title>
<link href="https://fonts.googleapis.com/css2?family=Inter:wght@300;400;500;600&display=swap" rel="stylesheet">
<style>
:root{
  --navy:#1f2a44;
  --navy-deep:#18213a;
  --band:#232e4a;
  --green:#5fe08c;
  --teal:#3fd3a4;
  --ice:#eaf2f4;
  --ink:#1b2233;
  --muted:#4a5163;
  --line:#c9ced8;
  --white:#ffffff;
}
*{box-sizing:border-box;margin:0;padding:0}
html,body{width:1200px;height:4469px;overflow:hidden}
body{position:relative;background:var(--white);font-family:"Inter",Arial,sans-serif;color:var(--ink)}
.abs{position:absolute}
a{color:inherit;text-decoration:none}

/* header */
.site-header{position:absolute;left:0;top:0;width:1200px;height:116px;background:var(--white)}
.brand{position:absolute;left:48px;top:34px;display:flex;align-items:center;gap:10px}
.brand-mark{width:34px;height:34px;background:var(--navy)}
.brand-name{font-size:30px;font-weight:500;color:var(--navy);line-height:1}
.brand-sub{display:block;font-size:8px;font-weight:500;letter-spacing:.5px;color:var(--navy);margin-top:4px}
.header-divider{position:absolute;left:229px;top:0;width:1px;height:116px;background:#e3e6ec}
.topbar{position:absolute;left:240px;top:16px;display:flex;gap:32px;font-size:11px;color:#7b8192}
.topbar span{display:flex;align-items:center;gap:6px}
.topbar-rule{position:absolute;left:229px;top:52px;width:971px;height:1px;background:#e3e6ec}
.social-top{position:absolute;right:74px;top:20px;display:flex;gap:14px}
.dot{width:12px;height:12px;border-radius:50%;background:#8a90a0}
.main-nav{position:absolute;left:266px;top:76px;display:flex;gap:42px;font-size:13px;font-weight:500;color:var(--ink)}
.btn-dark{display:inline-flex;align-items:center;gap:6px;background:var(--navy);color:var(--white);border-radius:20px;font-size:12px;font-weight:500}
.header-cta{position:absolute;left:956px;top:64px;height:38px;padding:0 16px}

/* hero */
.hero{position:absolute;left:0;top:116px;width:1200px;height:581px;background:linear-gradient(180deg,#1a2240 0%,#2f3c6a 45%,#4a4f6c 70%,#2a2a35 100%)}
.hero-title{position:absolute;left:0;top:208px;width:1200px;text-align:center;font-size:54px;font-weight:300;line-height:64px;color:var(--white)}
.hero-btn{position:absolute;left:526px;top:363px;width:148px;height:36px;border-radius:18px;background:var(--green);color:var(--navy);font-size:16px;display:flex;align-items:center;justify-content:center}

/* about */
.map-deco{position:absolute;left:0;top:697px;width:700px;height:300px;background:radial-gradient(ellipse at 40% 40%,#eef1f4 0%,rgba(255,255,255,0) 70%)}
.photo-tower{position:absolute;left:92px;top:810px;width:132px;height:360px;background:linear-gradient(180deg,#a8b8cc,#3e5676)}
.photo-meeting{position:absolute;left:239px;top:850px;width:309px;height:360px;background:linear-gradient(180deg,#4c6a78,#1c2d34)}
.pill{display:inline-block;border:1.5px solid var(--navy);border-radius:22px;padding:9px 26px;font-size:16px;color:var(--navy)}
.about-pill{position:absolute;left:616px;top:798px}
.section-title{font-weight:300;color:var(--ink)}
.about-title{position:absolute;left:616px;top:858px;font-size:40px}
.about-copy{position:absolute;left:622px;top:928px;width:464px;font-size:12.5px;line-height:21.7px;color:var(--muted)}
.about-btn{position:absolute;left:616px;top:1149px;height:36px;padding:0 18px}
.stat{position:absolute;top:1262px;display:flex;align-items:center;gap:24px}
.stat-ring{position:relative;width:116px;height:116px}
.stat-ring svg{position:absolute;left:0;top:0}
.stat-value{position:absolute;left:0;top:0;width:116px;height:116px;display:flex;align-items:center;justify-content:center;font-size:28px;color:var(--ink)}
.stat-label{font-size:19px;color:var(--ink)}
.stat-note{font-size:12px;line-height:14px;color:var(--muted);width:160px;margin-top:6px}

/* team */
.team-band{position:absolute;left:0;top:1529px;width:1200px;height:538px;background:var(--ice)}
.team-pill{position:absolute;left:120px;top:1575px}
.team-title{position:absolute;left:120px;top:1655px;width:480px;font-size:39px;line-height:49px}
.team-copy{position:absolute;left:120px;top:1824px;width:470px;font-size:12.5px;line-height:21.7px;color:var(--muted)}
.founder-photo{position:absolute;left:645px;top:1465px;width:444px;height:574px;background:linear-gradient(160deg,#6c7889 0%,#4b596d 50%,#2f3a4d 100%)}
.founder-card{position:absolute;left:645px;top:1904px;width:161px;height:135px;background:var(--navy);color:var(--white);padding:26px 24px}
.founder-name{font-size:28px;font-weight:300}
.founder-role{font-size:11px;margin-top:6px;color:#c7cbd6}
.founder-social{width:12px;height:12px;background:var(--green);margin-top:16px}

/* investments */
.invest-band{position:absolute;left:0;top:2119px;width:1200px;height:529px;background:var(--band);overflow:hidden}
.invest-title{position:absolute;left:92px;top:116px;font-size:40px;font-weight:300;color:var(--white)}
.invest-copy{position:absolute;left:92px;top:182px;width:300px;font-size:12.5px;line-height:21.7px;color:#c9cedb}
.invest-card{position:absolute;top:73px;width:317px;height:360px;background:var(--white)}
.invest-img{height:213px;display:flex;align-items:center;justify-content:center;font-size:25px;font-weight:300;color:var(--white)}
.invest-body{padding:14px 22px}
.invest-name{font-size:12px;font-weight:600}
.invest-text{font-size:12.5px;line-height:15px;margin-top:14px;color:var(--ink)}

/* capabilities */
.cap-title{position:absolute;left:0;top:2708px;width:1200px;text-align:center;font-size:40px;font-weight:300}
.cap-card{position:absolute;color:var(--white);padding:0 28px}
.cap-card h3{font-size:27px;font-weight:300;margin-bottom:16px}
.cap-card p{font-size:12.5px;line-height:21.7px;color:#e3e6ee}

/* contact form */
.form-section{position:absolute;left:0;top:3593px;width:1200px;height:607px;background:linear-gradient(135deg,#e4ebf0 0%,#f3f6f8 55%,#dfe6ec 100%)}
.form-pill{position:absolute;left:485px;top:3703px;background:transparent}
.form-title{position:absolute;left:490px;top:3756px;font-size:40px}
.field-label{position:absolute;font-size:12.5px;color:var(--ink)}
.field-line{position:absolute;height:1px;background:#6b7283}
.submit-btn{position:absolute;left:472px;top:4078px;width:133px;height:35px;justify-content:center}

/* footer */
.site-footer{position:absolute;left:0;top:4200px;width:1200px;height:211px;background:var(--navy)}
.foot-col{position:absolute;top:50px;color:var(--white);font-size:12px}
.foot-col h4{color:var(--teal);font-size:16px;font-weight:400;margin-bottom:20px}
.foot-col li{list-style:none;display:flex;align-items:flex-start;gap:8px;margin-bottom:14px;line-height:16px}
.foot-links li{margin-bottom:8px;padding-left:6px}
.foot-social{display:flex;gap:10px;padding-left:4px}
.foot-social .dot{background:var(--white)}
.copyright{position:absolute;left:0;top:4411px;width:1200px;height:58px;background:var(--navy-deep);color:var(--white);font-size:12.5px;display:flex;align-items:center;justify-content:center}
</style>
</head>
<body>

<header class="site-header">
  <div class="brand">
    <div class="brand-mark"></div>
    <div><span class="brand-name">NVC</span><span class="brand-sub">CAPITAL MANAGEMENT</span></div>
  </div>
  <div class="header-divider"></div>
  <div class="topbar">
    <span><svg width="13" height="13" viewBox="0 0 24 24" fill="none" stroke="#7b8192" stroke-width="2"><path d="M12 22s7-7 7-12a7 7 0 0 0-14 0c0 5 7 12 7 12z"/><circle cx="12" cy="10" r="2.5"/></svg>Harbour Lane 12, 1230 Eastport</span>
    <span><svg width="14" height="12" viewBox="0 0 24 20" fill="none" stroke="#7b8192" stroke-width="2"><rect x="2" y="2" width="20" height="16" rx="2"/><path d="M2 4l10 7 10-7"/></svg>hello@northvale.com</span>
    <span><svg width="14" height="14" viewBox="0 0 24 24" fill="none" stroke="#7b8192" stroke-width="2"><path d="M22 17v3a2 2 0 0 1-2 2A19 19 0 0 1 2 4a2 2 0 0 1 2-2h3l2 5-2 1.5a12 12 0 0 0 7 7L15.5 13l5 2z"/></svg>+(100) 555-010-2030</span>
  </div>
  <div class="social-top"><span class="dot"></span><span class="dot"></span></div>
  <div class="topbar-rule"></div>
  <nav class="main-nav"><a>HOME</a><a>ABOUT US</a><a>PORTFOLIO</a><a>WHAT WE OFFER</a><a>CONTACT</a></nav>
  <a class="btn-dark header-cta">GET IN TOUCH <svg width="10" height="10" viewBox="0 0 10 10" stroke="#fff" stroke-width="1.3" fill="none"><path d="M2 8L8 2M3 2h5v5"/></svg></a>
</header>

<section class="hero" role="img" aria-label="Night skyline of a waterfront city with a lit bridge">
  <h1 class="hero-title">Passion for Uncovering<br>New Opportunities</h1>
  <a class="hero-btn">Get in touch</a>
</section>

<div class="map-deco" role="img" aria-label="Faint dotted world map"></div>
<div class="photo-tower" role="img" aria-label="Glass skyscraper seen from below"></div>
<div class="photo-meeting" role="img" aria-label="Business people in silhouette before market chart overlay"></div>
<span class="pill about-pill">WHO WE ARE</span>
<h2 class="section-title about-title">NVC Capital Management</h2>
<p class="about-copy">A beacon of innovative investment where strategic diversification meets meticulous market comprehension. We navigate the complexities of Global Equities, Real Estate, Venture Capital, Private Equity, and Alternative Assets, focusing on uncovering distinctive investment opportunities for our investors. At NVC, investment is not just a transaction; it's a carefully orchestrated process, mirroring the meticulous management of personal assets. Our ethos is built on a bedrock of expansive market wisdom and proactive strategy formulation, ensuring our portfolio remains both robust and agile.</p>
<a class="btn-dark about-btn">LEARN MORE <svg width="10" height="10" viewBox="0 0 10 10" stroke="#fff" stroke-width="1.3" fill="none"><path d="M2 8L8 2M3 2h5v5"/></svg></a>

<div class="stat" style="left:100px">
  <div class="stat-ring"><svg width="116" height="116"><circle cx="58" cy="58" r="54" fill="none" stroke="#e2e5ea" stroke-width="4"/><circle cx="58" cy="58" r="54" fill="none" stroke="#5fe08c" stroke-width="4" stroke-dasharray="203.6 339.3" transform="rotate(-90 58 58)"/></svg><div class="stat-value">60%</div></div>
  <div><div class="stat-label">Completed work</div><div class="stat-note">Quis nostrud exercitation ullamco sed do eiusmod tempor.</div></div>
</div>
<div class="stat" style="left:434px">
  <div class="stat-ring"><svg width="116" height="116"><circle cx="58" cy="58" r="54" fill="none" stroke="#e2e5ea" stroke-width="4"/><circle cx="58" cy="58" r="54" fill="none" stroke="#5fe08c" stroke-width="4" stroke-dasharray="186.6 339.3" transform="rotate(-90 58 58)"/></svg><div class="stat-value">55 %</div></div>
  <div><div class="stat-label">Active to work</div><div class="stat-note">Quis nostrud exercitation ullamco sed do eiusmod tempor.</div></div>
</div>
<div class="stat" style="left:772px">
  <div class="stat-ring"><svg width="116" height="116"><circle cx="58" cy="58" r="54" fill="none" stroke="#e2e5ea" stroke-width="4"/><circle cx="58" cy="58" r="54" fill="none" stroke="#5fe08c" stroke-width="4" stroke-dasharray="271.4 339.3" transform="rotate(-90 58 58)"/></svg><div class="stat-value">80%</div></div>
  <div><div class="stat-label">Goals Priority</div><div class="stat-note">Quis nostrud exercitation ullamco sed do eiusmod tempor.</div></div>
</div>

<div class="team-band"></div>
<span class="pill team-pill">OUR TEAM</span>
<h2 class="section-title team-title">(Meet our founder): The Architect of NVC's Visionary Path</h2>
<p class="team-copy">Meet Marc, the driving force behind NVC Capital Management. From co-founding Australia's second-largest renewable energy company to pioneering ventures in diverse sectors, Marc's entrepreneurial journey is marked by a passion for market innovation and sustainable growth. With over a decade of diverse business scaling experience, Marc established NVC Capital, evolving from personal investment to a trust-fortified endeavour of market innovation and niche investment exploration.</p>
<div class="founder-photo" role="img" aria-label="Portrait of the founder in a grey suit, arms crossed"></div>
<div class="founder-card"><div class="founder-name">Marc T.</div><div class="founder-role">Founder</div><div class="founder-social"></div></div>

<section class="invest-band">
  <h2 class="invest-title">Investments</h2>
  <p class="invest-copy">Lorem ipsum dolor sit amet consectetur. Mi eu etiam sed tincidunt risus ultrices. Commodo quis semper mauris orci ut. Nisi amet at praesent facilisis integer. Euismod diam pretium cursus sed massa sagittis purus eget. Amet amet lorem porta ac. Ac et sit aliquam tincidunt. Viverra aenean ipsum ullamcorper vel erat aenean donec egestas.</p>
  <article class="invest-card" style="left:463px">
    <div class="invest-img" role="img" aria-label="Hotel bedroom interior" style="background:linear-gradient(180deg,#5a5660,#8a7a6a)">Staynest</div>
    <div class="invest-body"><div class="invest-name">STAYNEST</div><p class="invest-text">Staynest is an online community marketplace for people to list, discover, and book accommodations through mobile phones or the</p></div>
  </article>
  <article class="invest-card" style="left:798px">
    <div class="invest-img" role="img" aria-label="Glass office headquarters building" style="background:linear-gradient(180deg,#3c4a74,#6a7ba0)">Linkwave</div>
    <div class="invest-body"><div class="invest-name">STAYNEST</div><p class="invest-text">Staynest is an online community marketplace for people to list, discover, and book accommodations through mobile phones or the</p></div>
  </article>
  <article class="invest-card" style="left:1131px">
    <div class="invest-img" role="img" aria-label="Glass tower facade" style="background:linear-gradient(180deg,#9fb0c4,#5a6d86)"></div>
    <div class="invest-body"><div class="invest-name">STAYNEST</div><p class="invest-text">Staynest is an online community marketplace for people to list, discover, and book accommodations through mobile phones or the</p></div>
  </article>
</section>

<h2 class="cap-title">Our capabilities</h2>
<div class="cap-card" role="img" aria-label="Blue skyscrapers with light trails" style="left:92px;top:2793px;width:373px;height:342px;background:linear-gradient(180deg,#4a6aa8 0%,#2b3b6a 60%,#223056 100%);padding-top:156px">
  <h3>Venture Capital</h3><p>Strategic investments in venture capital, where we harness our industry contacts and market understanding to invest in high growth startups and businesses.</p>
</div>
<div class="cap-card" role="img" aria-label="Team meeting in a glass office" style="left:482px;top:2793px;width:607px;height:342px;background:linear-gradient(180deg,#6a8094 0%,#3d5168 55%,#2a3a54 100%);padding-top:196px;padding-left:50px">
  <h3>Private Equity</h3><p>Strategic investments in venture capital, where we harness our industry contacts<br>and market understanding to invest in high growth startups and businesses.</p>
</div>
<div class="cap-card" role="img" aria-label="Stock chart over a city at dusk" style="left:92px;top:3156px;width:607px;height:340px;background:linear-gradient(180deg,#3c6070 0%,#2e4458 50%,#24304e 100%);padding-top:186px;padding-left:46px">
  <h3>Global Equity Markets</h3><p>We've demonstrated exceptional skill in identifying undervalued stocks and<br>markets with high growth potential, leveraging in-depth research and market<br>analysis</p>
</div>
<div class="cap-card" role="img" aria-label="Engineer at a construction site with cranes" style="left:716px;top:3156px;width:373px;height:340px;background:linear-gradient(180deg,#6d8aa0 0%,#445a78 55%,#27345a 100%);padding-top:150px;padding-left:22px">
  <h3>Property Development</h3><p>Curated development projects, exemplifying our ability to identify and capitalise on high-value real estate opportunities.</p>
</div>

<section class="form-section" role="img" aria-label="Faded upward view of a modern building"></section>
<span class="pill form-pill">BEACOME A CLIENT</span>
<h2 class="section-title form-title">Ready to Get Started</h2>
<span class="field-label" style="left:484px;top:3842px">Your Name*</span>
<div class="field-line" style="left:484px;top:3879px;width:255px"></div>
<span class="field-label" style="left:794px;top:3840px">Phone number</span>
<div class="field-line" style="left:794px;top:3876px;width:257px"></div>
<span class="field-label" style="left:484px;top:3906px">Your email*</span>
<div class="field-line" style="left:484px;top:3943px;width:556px"></div>
<span class="field-label" style="left:484px;top:3970px">Message</span>
<div class="field-line" style="left:484px;top:4061px;width:556px"></div>
<a class="btn-dark submit-btn">SUBMIT <svg width="10" height="10" viewBox="0 0 10 10" stroke="#fff" stroke-width="1.3" fill="none"><path d="M2 8L8 2M3 2h5v5"/></svg></a>

<footer class="site-footer">
  <div class="foot-col" style="left:498px">
    <h4>CONTACT US</h4>
    <ul>
      <li><svg width="18" height="18" viewBox="0 0 24 24" fill="none" stroke="#fff" stroke-width="2"><path d="M22 17v3a2 2 0 0 1-2 2A19 19 0 0 1 2 4a2 2 0 0 1 2-2h3l2 5-2 1.5a12 12 0 0 0 7 7L15.5 13l5 2z"/></svg>+(100) 555-010-2030</li>
      <li><svg width="18" height="15" viewBox="0 0 24 20" fill="none" stroke="#fff" stroke-width="2"><rect x="2" y="2" width="20" height="16" rx="2"/><path d="M2 4l10 7 10-7"/></svg>hello@northvale.com</li>
      <li><svg width="18" height="18" viewBox="0 0 24 24" fill="none" stroke="#fff" stroke-width="2"><path d="M12 22s7-7 7-12a7 7 0 0 0-14 0c0 5 7 12 7 12z"/><circle cx="12" cy="10" r="2.5"/></svg>Harbour Lane 12,<br>1230 Eastport</li>
    </ul>
  </div>
  <div class="foot-col foot-links" style="left:754px">
    <h4>QUICKLINKS</h4>
    <ul><li>Home</li><li>About us</li><li>What we offer</li><li>Contact</li></ul>
  </div>
  <div class="foot-col" style="left:988px;top:58px">
    <h4>FOLLOW US</h4>
    <div class="foot-social"><span class="dot"></span><span class="dot"></span></div>
  </div>
</footer>
<div class="copyright">Copyright © 2023 Northvale, All Rights Reserved.</div>

</body>
</html>
```